Premium Food Label Design – High-End Boutique Jar Labels (3 Sizes)

I require a complete jar label redesign across three sizes:
75mm x 130mm (Large & Medium)
55mm x 120mm (Small)
45mm x 120mm (XS)

The design must feel professional, modern, elegant, and high-end boutique.
Primary aesthetic: white, minimal, refined, with accents in soft brown and gold/bronze. (see prefer colours of logo in OLD LABEL PDF)
Transparent background required.

I have attached my current label for wording reference only — I want to move away from the kraft look entirely.
The label must include all existing details, plus a dedicated space to manually add batch number and date.

IMPORTANT: Final files must be supplied as editable Adobe Illustrator (.AI) files with live text layers (not outlined) so I can update them as needed.
Logo is attached. I’m open to a fresh, elevated design direction aligned with a premium brand feel.
Updates

Low design quality

Target Market(s)

People who appreciate high-end, thoughtfully crafted food and are willing to pay for quality

Industry/Entity Type

Gourmet Food / Artisan Food Packaging

Requirements
Must have
• Premium, minimal aesthetic, Strong typography hierarchy, White background, Consistency across 3 sizes
Nice to have
• Elevated “Velvet Orchard” styling
Should not have
• No bright or bold colours, No clutter or overcrowding, No heavy borders or thick frames,No “homemade/craft” fonts

```html
<!DOCTYPE html>
<html lang="en">
<head>
<meta charset="utf-8">
<title>Tomato Relish – Jar Label</title>
<link href="https://fonts.googleapis.com/css2?family=Cormorant+Garamond:wght@500;700&family=Encode+Sans+Semi+Expanded:wght@400;700&display=swap" rel="stylesheet">
<style>
  :root {
    --paper: #ffffff;
    --stage: #ffffff;
    --olive: #66703a;
    --sage: #9aab72;
    --brown: #44261b;
    --sage-faint: #c2cca6;
    --rule: #5a5a5a;
  }
  * { margin: 0; padding: 0; box-sizing: border-box; }
  html, body {
    width: 920px; height: 1200px; overflow: hidden;
    background: var(--stage);
  }
  .canvas { position: relative; width: 920px; height: 1200px; }
  .label {
    position: absolute; width: 376px; height: 651px;
    background: var(--paper);
    box-shadow: 0 4px 18px rgba(0,0,0,0.16);
  }
  .label--front { left: 78px; top: 100px; }
  .label--back { left: 477px; top: 399px; }

  .sans {
    font-family: "Encode Sans Semi Expanded", sans-serif;
    font-variant: small-caps;
  }
  .serif { font-family: "Cormorant Garamond", serif; }

  .arch { position: absolute; left: 0; top: 0; }
  .brand-name {
    position: absolute; left: 0; width: 376px; top: 110px;
    text-align: center; color: var(--brown);
    font-size: 22px; font-weight: 400; letter-spacing: 2px;
  }
  .kicker {
    position: absolute; left: 0; width: 376px; top: 270px;
    text-align: center; color: var(--olive);
    font-size: 26px; letter-spacing: 0.5px;
  }
  .product-name {
    position: absolute; left: 0; width: 376px; top: 320px;
    text-align: center; color: var(--brown);
    font-size: 62px; font-weight: 700; line-height: 58px; letter-spacing: 1px;
  }
  .tagline {
    position: absolute; left: 96px; top: 474px; width: 254px; height: 50px;
    background: var(--olive); color: var(--paper);
    display: flex; align-items: center; justify-content: center;
    font-size: 25px; letter-spacing: 0.5px;
  }
  .weight-row {
    position: absolute; left: 96px; top: 568px; width: 258px; height: 40px;
    display: flex; align-items: center; justify-content: space-between;
  }
  .weight-row .rule { width: 68px; height: 1px; background: var(--rule); }
  .weight {
    color: var(--olive); font-size: 34px; font-weight: 500;
  }

  .back-title {
    position: absolute; left: 0; width: 376px; top: 56px;
    text-align: center; color: var(--brown);
    font-size: 28px; font-weight: 700; letter-spacing: 1px;
  }
  .intention {
    position: absolute; left: 48px; width: 280px; top: 114px;
    text-align: center; color: var(--brown);
    font-size: 14px; line-height: 21px;
  }
  .back-mark {
    position: absolute; left: 0; width: 376px; top: 244px;
    text-align: center; color: var(--sage-faint);
    font-size: 14px; letter-spacing: 1px;
  }
  .facts {
    position: absolute; left: 41px; width: 290px;
    color: var(--brown); font-size: 14.5px; line-height: 21px;
  }
  .facts b { font-weight: 700; }
  .facts--ingredients { top: 298px; }
  .facts--storage { top: 372px; }
  .fill-row {
    position: absolute; left: 41px; top: 465px; width: 296px;
    display: flex; align-items: baseline; color: var(--olive);
    font-size: 17px;
  }
  .fill-row .blank {
    display: inline-block; width: 86px; border-bottom: 1px solid var(--rule);
    margin: 0 16px 0 10px; transform: translateY(-5px);
  }
  .fill-row .blank:last-child { margin-right: 0; }
  .maker {
    position: absolute; left: 0; width: 376px; top: 504px;
    text-align: center; color: var(--olive);
    font-size: 17px; line-height: 24px;
  }
  .maker b { font-weight: 700; }
  .maker-rule {
    position: absolute; left: 41px; width: 293px; top: 557px;
    height: 1.5px; background: var(--olive);
  }
  .contact {
    position: absolute; left: 0; width: 376px; top: 564px;
    text-align: center; color: var(--brown);
    font-size: 18px; line-height: 22px;
  }
</style>
</head>
<body>
<div class="canvas">

  <section class="label label--front">
    <svg class="arch" width="376" height="260" viewBox="0 0 376 260" aria-hidden="true">
      <path d="M62 0 V126 A125 125 0 0 0 312 126 V0" fill="none" stroke="var(--olive)" stroke-width="1.2"/>
      <path d="M70 0 V126 A117 117 0 0 0 304 126 V0" fill="none" stroke="var(--sage)" stroke-width="3.5"/>
    </svg>
    <div class="brand-name sans">Hearth &amp; Grain</div>
    <div class="kicker sans">Popular Choice</div>
    <h1 class="product-name serif">TOMATO<br>RELISH</h1>
    <div class="tagline sans">Made with love</div>
    <div class="weight-row">
      <span class="rule"></span>
      <span class="weight serif">375g</span>
      <span class="rule"></span>
    </div>
  </section>

  <section class="label label--back">
    <h2 class="back-title serif">VELVET ORCHARD</h2>
    <p class="intention sans">What is made with love is felt in return. May this relish nourish more than the meal —bringing comfort, connection, and joy to every moment shared.</p>
    <div class="back-mark sans">Hearth &amp; Grain</div>
    <p class="facts facts--ingredients sans"><b>Ingredients:</b> Tomatoes, onion, sugar, vinegar, salt, spices, thickener (cornflour)</p>
    <p class="facts facts--storage sans"><b>Storage:</b> Keep refrigerated once opened</p>
    <div class="fill-row sans">Batch:<span class="blank"></span>Date:<span class="blank"></span></div>
    <p class="maker sans">Made by <b>Hearth &amp; Grain,</b><br>QLD, Australia</p>
    <div class="maker-rule"></div>
    <p class="contact sans">W: hearthandgrain.com<br>E: hello@hearthandgrain.com</p>
  </section>

</div>
</body>
</html>
```